Binder design for a veterinary clinic

We are seeking a talented designer to create a standout design for ring binders specifically for our veterinary clinic. These binders will be used to organize materials from our Continuing Professional Development (CPD) projects for colleagues and interns. The design should be clean, professional, and align with our brand guidelines. To give you a better understanding of our branding, we’ve included the design of our vehicles as a reference. As additional reference, please visit www.tierpraxolend.at

Target Market(s)

veterinarians

Industry/Entity Type

Veterinary

Font styles to use
Sans Serif

Colors
0054AA
0677BA
7BADD7
CADEEF
E8F1F8
FFC000
F8CF3A
FAE287
FDF2CF
FEFAEE

Requirements
Must have
• Our Logo an a clean design
Should not have
• to much images

```html
<!DOCTYPE html>
<html lang="de">
<head>
<meta charset="utf-8">
<title>Tierpraxolend – Ordner</title>
<link href="https://fonts.googleapis.com/css2?family=Outfit:wght@700&family=Montserrat:wght@600&family=Barlow:wght@500&display=swap" rel="stylesheet">
<style>
  :root{
    --bg:#e9e9e9;
    --navy:#34495a;
    --navy-dark:#263848;
    --gold:#c9952b;
    --gold-light:#d2a23c;
    --white:#ffffff;
    --photo-top:#8f9396;
    --photo-bottom:#6c7073;
  }
  html,body{margin:0;padding:0;width:1200px;height:960px;overflow:hidden;background:var(--bg);}
  .binder{position:absolute;left:235px;top:70px;width:730px;height:820px;display:flex;box-shadow:0 20px 40px rgba(0,0,0,.15);}
  .spine{width:110px;height:820px;display:block;}
  .cover{width:620px;height:820px;display:block;}
  .brand-name{font-family:'Outfit',sans-serif;font-weight:700;fill:var(--white);}
  .brand-tagline{font-family:'Montserrat',sans-serif;font-weight:600;fill:var(--gold);}
  .contact-text{font-family:'Barlow',sans-serif;font-weight:500;font-size:17px;fill:var(--navy-dark);}
</style>
</head>
<body>
<div class="binder">
  <svg class="spine" viewBox="0 0 110 820" xmlns="http://www.w3.org/2000/svg">
    <rect class="spine-base" width="110" height="820" fill="var(--navy-dark)"/>
    <path class="spine-gold" d="M0 655 Q55 635 110 640 L110 820 L0 820Z" fill="var(--gold)"/>
    <path class="spine-stripe" d="M0 652 Q55 632 110 637" fill="none" stroke="var(--white)" stroke-width="4"/>
    <g transform="translate(60 330) rotate(-90)">
      <text class="brand-name" x="0" y="0" font-size="34" text-anchor="middle">Tierpraxolend</text>
      <text class="brand-tagline" x="0" y="24" font-size="13" text-anchor="middle">Fachklinik für Kleintiere</text>
    </g>
    <circle class="spine-mark" cx="55" cy="490" r="36" fill="none" stroke="var(--white)" stroke-width="5"/>
  </svg>

  <svg class="cover" viewBox="0 0 620 820" xmlns="http://www.w3.org/2000/svg">
    <defs>
      <linearGradient id="photoTone" x1="0" y1="0" x2="0" y2="1">
        <stop offset="0" stop-color="var(--photo-top)"/>
        <stop offset="1" stop-color="var(--photo-bottom)"/>
      </linearGradient>
    </defs>
    <rect class="cover-base" width="620" height="820" fill="var(--navy)"/>

    <polygon class="corner-stripe" points="385,0 440,0 620,150 620,178" fill="var(--white)"/>
    <polygon class="corner-gold" points="470,0 620,0 620,140" fill="var(--gold-light)"/>

    <circle class="brand-mark" cx="310" cy="150" r="64" fill="none" stroke="var(--white)" stroke-width="7"/>
    <text class="brand-name" x="310" y="300" font-size="56" text-anchor="middle">Tierpraxolend</text>
    <text class="brand-tagline" x="310" y="330" font-size="19" text-anchor="middle">Fachklinik für Kleintiere</text>

    <polygon class="clinic-photo" role="img" aria-label="Foto des Klinikgebäudes mit Fassadenschriftzug" points="150,470 620,380 620,820 150,820" fill="url(#photoTone)"/>

    <polygon class="band-white" points="0,588 620,780 620,820 0,820" fill="var(--white)"/>
    <polygon class="band-navy" points="0,600 600,820 0,820" fill="var(--navy-dark)"/>
    <polygon class="band-gold" points="0,612 545,820 0,820" fill="var(--gold)"/>

    <g class="contact">
      <g class="contact-phone" transform="translate(38 692)">
        <circle r="13" fill="var(--navy-dark)"/>
        <path d="M-5 -6 q2 -1 3 1 l1 3 q0 1 -1 2 q1 3 4 4 q1 -1 2 -1 l3 1 q2 1 1 3 q-1 2 -3 2 q-7 -1 -11 -9 q-1 -4 1 -6z" fill="var(--white)"/>
        <text class="contact-text" x="24" y="6">+43(0)1 55210</text>
      </g>
      <g class="contact-mail" transform="translate(38 738)">
        <circle r="13" fill="var(--navy-dark)"/>
        <rect x="-7" y="-5" width="14" height="10" fill="none" stroke="var(--white)" stroke-width="1.6"/>
        <path d="M-7 -5 L0 1 L7 -5" fill="none" stroke="var(--white)" stroke-width="1.6"/>
        <text class="contact-text" x="24" y="6">info@tierpraxolend.at</text>
      </g>
      <g class="contact-address" transform="translate(38 785)">
        <circle r="13" fill="var(--navy-dark)"/>
        <path d="M0 8 C-6 1 -6 -2 -6 -3 a6 6 0 0 1 12 0 c0 1 0 4 -6 11z" fill="var(--white)"/>
        <circle cy="-3" r="2.2" fill="var(--navy-dark)"/>
        <text class="contact-text" x="24" y="-2">Tierpraxolend GmbH &amp; Co KG</text>
        <text class="contact-text" x="24" y="18">Lindenweg 14B 1100 Vienna</text>
      </g>
    </g>
  </svg>
</div>
</body>
</html>
```